Project Overview:
We are looking to create a website for a monthly subscription IPTV service in WordPress. The website should provide a seamless user experience for customers to sign up for the service and manage their account information. We need the following pages: Home Page, Product Page, Sign-Up Page, and Account Information Page.

Home Page:
The Home Page design should be simple and clean, with a dark theme and minimalistic design elements. We would like to include graphics of popular movie shows displayed on multiple devices. The page should highlight the key benefits and features of our service and provide a clear call-to-action for visitors to sign up.

Product Page:
The Product Page should provide detailed information about our subscription tiers and pricing plans. It should highlight the key features of each plan and provide a clear comparison between them. The page should also include a call-to-action button for visitors to sign up.

Sign-Up Page:
The Sign-Up Page is the conversion page where members will sign up for the service. It should collect the following information: Name, Phone Number, Email, Password, and Payment Information. The design should be simple, intuitive, and easy to use. It should highlight the benefits of our service and provide a clear call-to-action for visitors to sign up.

Account Information Page:
The Account Information Page should allow members to view and manage their account details. It should include the following information: Profile Image, Contact Details, Password Management, Payment Information Management, and Membership Expiration Date. The design should be user-friendly, intuitive, and easy to navigate.

Goals: The primary goal of the website is to provide an easy-to-use portal for customers to sign up for the service and manage their account information. The website should be user-friendly and visually appealing to attract potential customers.

Scope: The scope of the project includes designing a home page, a sign-up page, an account information page, and a payment information page. The website should be designed to be responsive and accessible on desktop and mobile devices.

Design Preferences: The design should be clean, modern, and visually appealing. The use of a color palette that is consistent with the brand identity is recommended. The website should be easy to navigate and provide a clear call-to-action for users to sign up for the service.

FYI: The subscription service I am designing a website for is related to an IPTV service. IPTV stands for Internet Protocol Television, which is a digital television broadcasting protocol that uses the internet to deliver TV programs and videos to viewers. The website will allow customers to sign up for the IPTV service and access their account information such as user name and password, membership tier, name, and payment details. Please let me know if you have any further questions, and I would be happy to provide more details. Thank you!

Dear Designers,

Thank you for your participation in our project. After reviewing the designs received so far, we have decided to update the brief to better reflect our needs and preferences. We apologize for any confusion this may cause, but we believe that these changes will result in better design submissions and a more successful project overall.

The updated brief is as follows:

We are looking to create a website for WordPress.

Also, here is the updated Brief.

Project Title: WordPress Website Design for Monthly Subscription IPTV Service

Project Overview:
We are looking to create a website for a monthly subscription IPTV service. The website should provide a seamless user experience for customers to sign up for the service and manage their account information. We need the following pages: Home Page, Product Page, Sign-Up Page, and Account Information Page.

Home Page:

Product Page:

Sign-Up Page:

Account Information Page:

Design Preferences:
We prefer a dark theme with minimalistic design elements and hits of our logo colors. The website should be easy to use and navigate, with clear calls-to-action and simple, intuitive forms. The design should be optimized for mobile devices and load quickly.

We hope that these updates provide you with a clearer understanding of our requirements and preferences. Please let us know if you have any questions or concerns. We look forward to seeing your revised designs.

Thank you again for your participation.
We will guarantee this project as soon as we see something we like that meets the updated requirements.

The website's target audience is individuals who are interested in subscribing to the monthly service.

Coded - Design and coding required

4 page

Designer to choose colors to be used in the design.

• One item for sale and a client profile section.

```html
<!DOCTYPE html>
<html lang="en">
<head>
<meta charset="utf-8">
<title>VELORA – IPTV Subscription</title>
<link href="https://fonts.googleapis.com/css2?family=Kanit:ital,wght@1,800;1,900&family=Roboto:wght@400;500;700;900&display=swap" rel="stylesheet">
<style>
:root{
  --red:#ff0a0a;
  --red-dark:#c40000;
  --black:#000;
  --panel:#0d0d0d;
  --band:#151515;
  --text:#fff;
  --muted:#d6d6d6;
}
*{box-sizing:border-box;margin:0;padding:0}
html,body{width:1200px;height:4083px;overflow:hidden;background:var(--black)}
body{font-family:"Roboto",Arial,sans-serif;color:var(--text);position:relative}
.abs{position:absolute}
.heading{font-family:"Kanit","Arial Black",sans-serif;font-style:italic;font-weight:900;color:var(--red);text-shadow:2px 2px 0 #fff;letter-spacing:.5px}
.btn{position:absolute;display:flex;align-items:center;justify-content:center;gap:9px;background:var(--red);color:#fff;font-weight:700;font-size:15px;text-transform:uppercase;border-radius:3px}
.btn .dot{width:14px;height:14px;border-radius:50%;background:#fff;display:inline-flex;align-items:center;justify-content:center}
.btn .dot svg{width:8px;height:8px}

/* header */
.site-header{left:0;top:0;width:1200px;height:80px;background:#000}
.logo{font-family:"Roboto",sans-serif;font-weight:900;font-size:40px;color:#fff;letter-spacing:1px}
.nav{top:30px;font-size:15px;font-weight:500}
.nav .active{color:var(--red)}

/* hero */
.hero-photo{left:0;top:80px;width:1200px;height:612px;background:linear-gradient(100deg,#1d1a17 0%,#3b3027 28%,#2a4b58 60%,#1e7c93 85%,#0f4150 100%)}
.hero-shade{left:0;top:80px;width:700px;height:612px;background:linear-gradient(90deg,rgba(0,0,0,.55),rgba(0,0,0,0))}
.hero-kicker{left:108px;top:242px;font-family:"Kanit",sans-serif;font-style:italic;font-weight:900;font-size:27px;color:#fff}
.hero-title{left:104px;top:272px;font-family:"Kanit",sans-serif;font-style:italic;font-weight:900;font-size:104px;line-height:1.1;color:#fff}
.hero-text{left:108px;top:402px;width:470px;font-size:15px;line-height:26px}

/* about */
.about-photo{left:102px;top:778px;width:478px;height:454px;border-radius:30px;background:linear-gradient(135deg,#b9a58c,#6e6356 45%,#cfd3d6 100%);box-shadow:-6px 6px 0 var(--red)}
.about-text{left:638px;top:862px;width:470px;font-size:15px;line-height:26px;text-align:justify;color:#f0f0f0}

/* features */
.features{left:0;top:1318px;width:1200px;height:614px;background:repeating-linear-gradient(125deg,#171717 0 80px,#121212 80px 160px)}
.feature-card{top:1520px;width:313px;height:322px;background:#000;border-radius:60px 0 60px 0;text-align:center}
.feature-icon{position:absolute;left:110px;top:28px;width:94px;height:94px;border-radius:50%;background:#2b2b2b;display:flex;align-items:center;justify-content:center}
.feature-icon.on{background:var(--red)}
.feature-card h3{position:absolute;top:140px;width:100%;font-size:17px;font-weight:700}
.feature-card p{position:absolute;top:176px;left:20px;right:20px;font-size:14px;line-height:22px;color:var(--muted)}
.read-link{position:absolute;top:278px;width:100%;font-size:14px;font-weight:700;display:flex;justify-content:center;align-items:center;gap:7px}

/* shows */
.show-card{width:307px;background:var(--panel);border-radius:12px;text-align:center}
.show-photo{position:absolute;left:7px;top:8px;width:293px;height:228px;border-radius:10px}
.show-card h4{position:absolute;top:272px;width:100%;font-size:14px;font-weight:500;text-transform:uppercase}
.show-card p{position:absolute;top:300px;left:18px;right:18px;font-size:14px;line-height:24px;color:var(--muted)}
.outline-btn{position:absolute;left:88px;top:392px;width:134px;height:42px;border:1px solid #7a0d0d;border-radius:3px;font-size:14px;font-weight:700;display:flex;align-items:center;justify-content:center}
.arrow{top:2296px}

/* benefits */
.benefit-photo{left:0;top:2680px;width:594px;height:535px;background:linear-gradient(120deg,#3e3528,#6b5844 40%,#2a2520 75%,#14110e)}
.benefit-band{left:594px;top:2680px;width:606px;height:535px;background:linear-gradient(135deg,#121212,#1c1c1c 50%,#0c0c0c)}
.benefit-list{left:680px;top:2790px;list-style:none;font-size:15px}
.benefit-list li{display:flex;align-items:center;gap:14px;height:43px}

/* signup */
.signup{left:0;top:3215px;width:1200px;height:485px;background:radial-gradient(ellipse at center,#121212,#050505)}
.signup-title{left:0;top:3290px;width:1200px;text-align:center;font-family:"Kanit",sans-serif;font-style:italic;font-weight:800;font-size:34px;color:var(--red)}
.signup-text{left:162px;top:3366px;width:876px;text-align:center;font-size:15px;line-height:26px}

/* footer */
.footer{left:0;top:3700px;width:1200px;height:383px;background:radial-gradient(ellipse at 40% 70%,#1a1a1a,#000 70%)}
.foot-h{font-size:17px;font-weight:700}
.foot-small{font-size:13px;line-height:18px}
.foot-links{list-style:none;font-size:13px}
.foot-links li{height:33px}
.social{top:3812px;width:18px;height:18px;border-radius:50%;background:#fff}
</style>
</head>
<body>

<!-- header -->
<header class="abs site-header">
  <div class="abs logo" style="left:114px;top:15px">VELORA</div>
  <nav>
    <span class="abs nav active" style="left:604px">HOME</span>
    <span class="abs nav" style="left:686px">|</span>
    <span class="abs nav" style="left:724px">PRODUCT</span>
    <span class="abs nav" style="left:831px">|</span>
    <span class="abs nav" style="left:869px">SIGN UP</span>
  </nav>
  <div class="btn" style="left:957px;top:18px;width:132px;height:44px">LOGIN
    <svg width="13" height="14" viewBox="0 0 13 14"><circle cx="6.5" cy="4" r="3.5" fill="#fff"/><path d="M0 14c0-4 3-6 6.5-6S13 10 13 14z" fill="#fff"/></svg>
  </div>
</header>

<!-- hero -->
<section>
  <div class="abs hero-photo" role="img" aria-label="Friends laughing on a sofa while watching television in a living room"></div>
  <div class="abs hero-shade"></div>
  <div class="hero-kicker abs">WELCOME TO</div>
  <h1 class="hero-title abs">VELORA</h1>
  <p class="hero-text abs">Lorem ipsum dolor sit amet consectetur adipiscing elit sed do eiusmod tempor incididunt ut labore et dolore magna aliqua.</p>
  <div class="btn" style="left:108px;top:478px;width:160px;height:46px">GET STARTED <span class="dot"><svg viewBox="0 0 8 8"><path d="M2 1l4 3-4 3" stroke="#f00" stroke-width="1.6" fill="none"/></svg></span></div>
</section>

<!-- about -->
<section>
  <div class="abs about-photo" role="img" aria-label="Couple on a sofa browsing a streaming menu on a wall-mounted TV"></div>
  <h2 class="abs heading" style="left:638px;top:796px;font-size:36px">ABOUT VELORA</h2>
  <p class="abs about-text">Lorem ipsum dolor sit amet consectetur adipiscing elited sed do eiusmod tempor incididunt ut labore et dolore magna aliqua. Ut enim ad minim veniam, quis nostrud exercitation ullamco laboris nisi ut aliquip ex ea commodo consequat. Duis aute irure dolor in reprehenderit in voluptate velit esse cillum dolore eu fugiat nulla pariatur. Exceptteur sint occaecat cupidatat non proident, sunt in culpa qui officia deserunt mollit anim id est laborul.orem ipsum dolor sit amet, consectetur adipiscing elit, sed do eiusmod tempor incididunt ut labore et dolore magna aliqua. Ut enim ad minim veniam, nostrud exercitation ullamco laboris nisi aliquipcommodo consequat. Duis aute irure reprehenderit in voluptate velit esseg.</p>
  <div class="btn" style="left:638px;top:1175px;width:157px;height:45px">LEARN MOTRE <span class="dot"><svg viewBox="0 0 8 8"><path d="M2 1l4 3-4 3" stroke="#f00" stroke-width="1.6" fill="none"/></svg></span></div>
</section>

<!-- features -->
<section>
  <div class="abs features"></div>
  <h2 class="abs heading" style="left:0;top:1392px;width:1200px;text-align:center;font-size:36px">FEATURES OF OUR SERVICE</h2>

  <div class="abs feature-card" style="left:112px">
    <div class="feature-icon"><svg width="50" height="44" viewBox="0 0 50 44" fill="none" stroke="#f00" stroke-width="2"><rect x="8" y="8" width="34" height="24" rx="2"/><path d="M18 38h14M25 32v6"/><circle cx="25" cy="20" r="5"/></svg></div>
    <h3>Lorem ipsum dolor sit amet</h3>
    <p>Lorem ipsum dolor sit amet consectetur adipiscing eiusmoded tempor incididunt labore et dolore magna aliqua enim ad minim veniam nostrud exercitation.</p>
    <div class="read-link">READ MORE <span class="btn dot" style="position:static"><svg viewBox="0 0 8 8"><path d="M2 1l4 3-4 3" stroke="#000" stroke-width="1.6" fill="none"/></svg></span></div>
  </div>
  <div class="abs feature-card" style="left:443px">
    <div class="feature-icon on"><svg width="50" height="50" viewBox="0 0 50 50" fill="none" stroke="#fff" stroke-width="2"><rect x="8" y="8" width="30" height="22" rx="2"/><rect x="24" y="20" width="12" height="24" rx="3" fill="#f00"/><circle cx="30" cy="26" r="2"/></svg></div>
    <h3>Lorem ipsum dolor sit amet,</h3>
    <p>Lorem ipsum dolor sit amet consectetur adipiscing eiusmoded tempor incididunt labore et dolore magna aliqua enim ad minim veniam nostrud exercitation.</p>
    <div class="read-link">READ MORE <span class="btn dot" style="position:static"><svg viewBox="0 0 8 8"><path d="M2 1l4 3-4 3" stroke="#000" stroke-width="1.6" fill="none"/></svg></span></div>
  </div>
  <div class="abs feature-card" style="left:774px">
    <div class="feature-icon"><svg width="50" height="44" viewBox="0 0 50 44" fill="none" stroke="#f00" stroke-width="2"><rect x="6" y="6" width="38" height="26" rx="2"/><path d="M18 38h14M25 32v6"/><circle cx="25" cy="19" r="6"/></svg></div>
    <h3>Lorem ipsum dolor sit amet,</h3>
    <p>Lorem ipsum dolor sit amet consectetur adipiscing eiusmoded tempor incididunt labore et dolore magna aliqua enim ad minim veniam nostrud exercitation.</p>
    <div class="read-link">READ MORE <span class="btn dot" style="position:static"><svg viewBox="0 0 8 8"><path d="M2 1l4 3-4 3" stroke="#000" stroke-width="1.6" fill="none"/></svg></span></div>
  </div>
</section>

<!-- popular shows -->
<section>
  <h2 class="abs heading" style="left:0;top:2008px;width:1200px;text-align:center;font-size:36px">POPULAR MOVIE SHOWS</h2>
  <svg class="abs arrow" style="left:50px" width="16" height="22" viewBox="0 0 16 22"><path d="M12 2L4 11l8 9" stroke="#fff" stroke-width="2.5" fill="none"/></svg>
  <svg class="abs arrow" style="left:1134px" width="16" height="22" viewBox="0 0 16 22"><path d="M4 2l8 9-8 9" stroke="#fff" stroke-width="2.5" fill="none"/></svg>

  <article class="abs show-card" style="left:110px;top:2098px;height:470px">
    <div class="show-photo" role="img" aria-label="Hands holding a tablet playing a film" style="background:linear-gradient(135deg,#5c6f80,#c8ccd0 45%,#3a3a3a)"></div>
    <h4>Lorem ipsum dolor sit amet</h4>
    <p>Lorem ipsum dolor sit ametconsectetur adipiscing elited sed do eiusmod tempor incididunt ut labore eted dolore magna.</p>
    <div class="outline-btn">READ MORE</div>
  </article>
  <article class="abs show-card" style="left:446px;top:2100px;height:492px;background:#141414">
    <div class="show-photo" role="img" aria-label="Hands holding a phone showing a city video" style="top:30px;background:linear-gradient(135deg,#222,#9aa4ad 45%,#2b2b2b)"></div>
    <h4 style="top:296px">Lorem ipsum dolor sit amet</h4>
    <p style="top:324px">Lorem ipsum dolor sit ametconsectetur adipiscing elited sed do eiusmod tempor incididunt ut labore eted dolore magna.</p>
    <div class="outline-btn" style="top:416px">READ MORE</div>
  </article>
  <article class="abs show-card" style="left:783px;top:2098px;height:470px">
    <div class="show-photo" role="img" aria-label="Viewer with popcorn browsing films on a television" style="background:linear-gradient(135deg,#3a2c2a,#8a6a58 45%,#2a1e1a)"></div>
    <h4>Lorem ipsum dolor sit amet</h4>
    <p>Lorem ipsum dolor sit ametconsectetur adipiscing elited sed do eiusmod tempor incididunt ut labore eted dolore magna.</p>
    <div class="outline-btn">READ MORE</div>
  </article>
</section>

<!-- key benefit -->
<section>
  <div class="abs benefit-photo" role="img" aria-label="Person on a couch watching a wall of shows on a television in a warm lit room"></div>
  <div class="abs benefit-band"></div>
  <h2 class="abs heading" style="left:680px;top:2722px;font-size:36px">KEY BENEFIT</h2>
  <ul class="abs benefit-list">
    <li><svg width="14" height="14" viewBox="0 0 14 14"><circle cx="7" cy="7" r="6" fill="none" stroke="#f00" stroke-width="2"/><path d="M4 7l2 2 4-4" stroke="#f00" stroke-width="1.8" fill="none"/></svg>Lorem ipsum dolor sit amet consectetur adipiscing elit</li>
    <li><svg width="14" height="14" viewBox="0 0 14 14"><circle cx="7" cy="7" r="6" fill="none" stroke="#f00" stroke-width="2"/><path d="M4 7l2 2 4-4" stroke="#f00" stroke-width="1.8" fill="none"/></svg>Lorem ipsum dolor sit amet consectetur adipiscing elit</li>
    <li style="height:50px"><svg width="14" height="14" viewBox="0 0 14 14"><circle cx="7" cy="7" r="6" fill="none" stroke="#f00" stroke-width="2"/><path d="M4 7l2 2 4-4" stroke="#f00" stroke-width="1.8" fill="none"/></svg>Lorem ipsum dolor sit amet consectetur adipiscing elit</li>
    <li><svg width="14" height="14" viewBox="0 0 14 14"><circle cx="7" cy="7" r="6" fill="none" stroke="#f00" stroke-width="2"/><path d="M4 7l2 2 4-4" stroke="#f00" stroke-width="1.8" fill="none"/></svg>Lorem ipsum dolor sit amet consectetur adipiscing elit</li>
    <li><svg width="14" height="14" viewBox="0 0 14 14"><circle cx="7" cy="7" r="6" fill="none" stroke="#f00" stroke-width="2"/><path d="M4 7l2 2 4-4" stroke="#f00" stroke-width="1.8" fill="none"/></svg>Lorem ipsum dolor sit amet consectetur adipiscing elit</li>
    <li><svg width="14" height="14" viewBox="0 0 14 14"><circle cx="7" cy="7" r="6" fill="none" stroke="#f00" stroke-width="2"/><path d="M4 7l2 2 4-4" stroke="#f00" stroke-width="1.8" fill="none"/></svg>Lorem ipsum dolor sit amet consectetur adipiscing elit</li>
    <li><svg width="14" height="14" viewBox="0 0 14 14"><circle cx="7" cy="7" r="6" fill="none" stroke="#f00" stroke-width="2"/><path d="M4 7l2 2 4-4" stroke="#f00" stroke-width="1.8" fill="none"/></svg>Lorem ipsum dolor sit amet consectetur adipiscing elit</li>
  </ul>
  <div class="btn" style="left:680px;top:3113px;width:158px;height:46px">LEARN MOTRE <span class="dot"><svg viewBox="0 0 8 8"><path d="M2 1l4 3-4 3" stroke="#f00" stroke-width="1.6" fill="none"/></svg></span></div>
</section>

<!-- sign up -->
<section>
  <div class="abs signup"></div>
  <h2 class="abs signup-title">SIGN UP</h2>
  <p class="abs signup-text">Lorem ipsum dolor sit amet, consectetur adipiscing elit, sed do eiusmod tempor incididunt ut labore et dolore magna aliqua. Ut enim ad minim veniam, quis nostrud exercitation ullamco laboris nisi ut aliquip ex ea commodo consequat. Duis aute irure dolor in reprehenderit in voluptate velit esse cillum dolore eu fugiat nulla pariatur. Excepteur sint occaecat cupidatat non proident, sunt in culpa qui officia deserunt mollit anim id est laborum</p>
  <div class="btn" style="left:522px;top:3500px;width:156px;height:46px">LEARN MOTE <span class="dot"><svg viewBox="0 0 8 8"><path d="M2 1l4 3-4 3" stroke="#f00" stroke-width="1.6" fill="none"/></svg></span></div>
</section>

<!-- footer -->
<footer>
  <div class="abs footer"></div>
  <div class="abs logo" style="left:112px;top:3730px;font-size:44px">VELORA</div>
  <span class="abs social" style="left:146px"></span>
  <span class="abs social" style="left:177px"></span>
  <span class="abs social" style="left:208px"></span>
  <span class="abs social" style="left:241px"></span>

  <div class="abs foot-h" style="left:383px;top:3728px">Contact Us</div>
  <svg class="abs" style="left:384px;top:3772px" width="12" height="12" viewBox="0 0 12 12"><path d="M2 1l3 1-1 2 4 4 2-1 1 3-2 1C5 11 1 7 1 3z" fill="#f00"/></svg>
  <div class="abs foot-small" style="left:406px;top:3768px"><b>Phone</b><br>+1 888 888 8888</div>
  <svg class="abs" style="left:383px;top:3823px" width="14" height="10" viewBox="0 0 14 10"><rect width="14" height="10" rx="1" fill="#f00"/><path d="M0 0l7 5 7-5" stroke="#000" fill="none"/></svg>
  <div class="abs foot-small" style="left:406px;top:3818px"><b>Email</b><br>info@velora.tv</div>
  <svg class="abs" style="left:385px;top:3874px" width="10" height="14" viewBox="0 0 10 14"><path d="M5 0a5 5 0 0 1 5 5c0 4-5 9-5 9S0 9 0 5a5 5 0 0 1 5-5z" fill="#f00"/><circle cx="5" cy="5" r="2" fill="#000"/></svg>
  <div class="abs foot-small" style="left:406px;top:3870px"><b>Location</b><br>939 Lorem ipsum dolor sit amet<br>consectetur elited</div>

  <div class="abs foot-h" style="left:684px;top:3728px">Company</div>
  <ul class="abs foot-links" style="left:685px;top:3770px">
    <li>Home</li><li>About Us</li><li>Services</li><li>Blog</li><li>Contact us</li>
  </ul>

  <div class="abs foot-h" style="left:850px;top:3728px">Stil have questios?</div>
  <div class="abs foot-small" style="left:850px;top:3772px;width:240px;font-size:12px">Contact us using this form. A repesenta-tive will aswer your questions as soon as possible.</div>
  <div class="btn" style="left:850px;top:3857px;width:193px;height:42px;font-size:15px">GET IN TOUCH</div>

  <div class="abs" style="left:114px;top:3980px;width:976px;height:1px;background:#444"></div>
  <div class="abs" style="left:1012px;top:3970px;width:80px;height:19px;border-radius:10px;background:#3a3a3a;font-size:11px;display:flex;align-items:center;justify-content:center;gap:4px">&#8593; Go Up</div>
  <div class="abs foot-small" style="left:114px;top:4016px">© 2023 VELORA | All Rights Reserved</div>
  <div class="abs foot-small" style="left:765px;top:4016px">Privacy Policy &nbsp;|&nbsp; Cookie Policy &nbsp;|&nbsp; Terms Of Services</div>
</footer>

</body>
</html>
```